Bref créative
Modern Creative Stationary for Tech Start up!!!
TheByteDepot - Business cards - Letterheads - Email Signature -
Use same font as used in my logo
Smaller Text can be different- but in line with theme.
Professional
Pavel Orsk
Sales & Logistics
3rd Floor Birch Court
7X Fernhill Street
Harrow
London
HBX 8QW
0208 731 XXXX
07452168XXX
pavel@thebytedepotz.com
thebytedepotz.com
We want a double sided Business card that is elegant, modern, sleek and also creative. The logo should give you an idea of where we want to go in terms of theme.
Be creative, Be sexy and try your hardest as there is plenty more work to be done after this project.
This is our Logo.
We do not really like the shaded background. So it might be best to keep it flat black.
This is the white version of our Logo. It may be an idea to use this for the stationary.

```html
<!DOCTYPE html>
<html lang="en">
<head>
<meta charset="utf-8">
<title>TheByteDepot – Business Card</title>
<link href="https://fonts.googleapis.com/css2?family=Montserrat:wght@700&family=Open+Sans:wght@300;400&display=swap" rel="stylesheet">
<style>
  :root {
    --backdrop: #e6e6e6;
    --card: #0c0c0c;
    --card-edge: #1c1c1c;
    --white: #ffffff;
    --grey: #8c8c8c;
    --grey-dark: #5a5a5a;
    --rule: #262626;
    --accent: #2f9be0;
  }
  * { margin: 0; padding: 0; box-sizing: border-box; }
  html, body { width: 1200px; height: 1049px; overflow: hidden; }
  body {
    background: var(--backdrop);
    font-family: "Open Sans", Arial, sans-serif;
    position: relative;
  }
  .card {
    position: absolute;
    left: 250px;
    width: 700px;
    height: 400px;
    background: var(--card);
    border: 1px solid var(--card-edge);
    border-radius: 22px;
    overflow: hidden;
  }
  .card--front { top: 95px; }
  .card--back { top: 555px; }

  .brand {
    position: absolute;
    display: flex;
    align-items: center;
    gap: 14px;
    white-space: nowrap;
  }
  .brand__dot {
    flex: none;
    width: 48px; height: 48px;
    border-radius: 50%;
    background: var(--accent);
  }
  .brand__name {
    font-family: "Montserrat", Arial, sans-serif;
    font-weight: 700;
    font-size: 30px;
    line-height: 1;
    color: var(--white);
  }

  /* front */
  .person { position: absolute; left: 60px; top: 140px; }
  .person__name {
    font-weight: 300; font-size: 38px; color: var(--grey); line-height: 1.1;
  }
  .person__role {
    font-weight: 400; font-size: 13px; color: var(--grey-dark); margin-top: 6px;
  }
  .divider {
    position: absolute; left: 305px; top: 95px;
    width: 1px; height: 180px; background: var(--grey-dark);
  }
  .card--front .brand { left: 336px; top: 161px; }
  .address {
    position: absolute; left: 60px; right: 60px; top: 318px;
    border-top: 1px solid var(--rule); padding-top: 10px;
    font-size: 13px; color: var(--grey); text-align: right; line-height: 1.6;
  }

  /* back */
  .card--back .brand { left: 336px; top: 146px; }
  .contact {
    position: absolute; left: 398px; top: 282px;
    list-style: none; font-size: 13px; color: var(--grey);
  }
  .contact li { display: flex; align-items: center; gap: 10px; height: 24px; }
  .contact svg { width: 14px; height: 14px; fill: var(--accent); }
</style>
</head>
<body>

<section class="card card--front">
  <div class="person">
    <p class="person__name">Pavel Orsk</p>
    <p class="person__role">Sales &amp; Logistics</p>
  </div>
  <div class="divider"></div>
  <div class="brand">
    <span class="brand__dot"></span>
    <span class="brand__name">TheByteDepot</span>
  </div>
  <div class="address">
    <p>3rd Floor Birch Court 7X Fernhill Street Harrow London HBX 8QW</p>
    <p>www.thebytedepotz.com</p>
  </div>
</section>

<section class="card card--back">
  <div class="brand">
    <span class="brand__dot"></span>
    <span class="brand__name">TheByteDepot</span>
  </div>
  <ul class="contact">
    <li>
      <svg viewBox="0 0 16 16" aria-hidden="true"><rect x="4" y="1" width="8" height="14" rx="1.5"/></svg>
      07452168XXX
    </li>
    <li>
      <svg viewBox="0 0 16 16" aria-hidden="true"><path d="M4 1l3 3-2 2c1 2 3 4 5 5l2-2 3 3-2 3C7 15 1 9 1 3z"/></svg>
      0208 731 XXXX
    </li>
    <li>
      <svg viewBox="0 0 16 16" aria-hidden="true"><path d="M1 3h14v10H1z"/></svg>
      pavel@thebytedepotz.com
    </li>
  </ul>
</section>

</body>
</html>
```